Social Media Web Design

We require the design of 3 pages for our social media website. We have designed a general layout, which you can see at the link below:

https://files.plovari.com/folder/d/7QmZ204kwPtEcLsRRuMoPiWxYtV2/edit?usp=sharing

We need you to design the colour scheme, detailed layout and graphics. We will provide you with three basic HTML pages that will contain text and we would like you to return completed .css files. The html files are only to make your job simpler and to provide details. If it is easier for you to build the .css files from scratch then it is not necessary for you to use them. Also, if you would like to edit the html files feel free. We would like you to focus on the creative design component, specifically colours and graphics.

In terms of colours, we would like to avoid red and blue. We would also prefer not to have various shades of black and dark grey. We like strong, simple design colours that are easy on the eye.
**Update on Colour Themes**
Apologies, I feel that I wasn't entirely clear about the colours, specifically red, blue and black. We'd prefer to stay away from the use of red and blue as a major components of the theme. It is already used quite heavily in other social media sites and we're after a distinct look of our own. I didn't mean to suggest that no red or blue can be used in the design.
***

Some websites that we like the look of include:
https://velmora.com - We particularly like the layout and the colour scheme and contrasts. We would however, prefer to avoid blue themes.
www.brondiva.com
www.kaluthen.com
www.trepavine.com - The icons, images and style of this site are really good. As stated above, we'd prefer to avoid black though.

There is no need to design a primary website logo, but please design other icons, buttons and graphics.

We would prefer the page to be bold, modern and fun rather than professional. In addition, we like clean, uncluttered designs and designs that emphasize user experience. The Homepage listed is quite empty in terms of content, so you have freedom to be particularly creative on this page.

If you have any further questions please ask, we are very happy to provide any further details or help you might need.
Updates

Thanks in advance.

Target Market(s)

social media users

Industry/Entity Type

Media

Requirements
Must have
• We require css files at the end of the project.
We require the creation of every field in the design document to complete the project.
The spacial layout must replicate the design document.
Should not have
• Flash, Quarrendeck

```html
<!DOCTYPE html>
<html lang="en">
<head>
<meta charset="utf-8">
<title>Thornvale – Home</title>
<link rel="stylesheet" href="https://fonts.googleapis.com/css2?family=Fira+Sans+Extra+Condensed:wght@500;600;700&family=Source+Sans+3:wght@400;600;700&display=swap">
<style>
  :root {
    --purple-top: #8f72a2;
    --purple-bottom: #5d4470;
    --purple-panel: #8e6c9d;
    --purple-deep: #5a3478;
    --purple-title: #6a4a7e;
    --page-bg: #efeff2;
    --panel-frame: #dcdce0;
    --white: #ffffff;
    --ink: #222222;
    --field-text: #8a8a8a;
    --hero-green: #8fb054;
    --hero-light: #f4f4f6;
    --social-1: #2e4f86;
    --social-2: #7fb8c6;
    --social-3: #c0252a;
  }
  * { box-sizing: border-box; margin: 0; padding: 0; }
  html, body { width: 1200px; height: 768px; overflow: hidden; }
  body {
    position: relative;
    background: var(--page-bg);
    font-family: "Source Sans 3", Arial, sans-serif;
  }

  /* Header */
  .site-header {
    position: absolute; left: 0; top: 0; width: 1200px; height: 137px;
    background: linear-gradient(var(--purple-top), var(--purple-bottom));
    border-bottom: 2px solid #b9a6c6;
  }
  .brand {
    position: absolute; left: 121px; top: 45px;
    font-family: "Fira Sans Extra Condensed", sans-serif; font-weight: 700;
    font-size: 40px; line-height: 46px; letter-spacing: 0.5px; color: var(--white);
    white-space: nowrap;
  }
  .main-nav { position: absolute; left: 657px; top: 52px; display: flex; }
  .main-nav a {
    display: block; height: 38px; line-height: 38px; padding: 0 17px;
    color: var(--white); text-decoration: none; font-size: 19px; margin-right: 1px;
    border-radius: 6px; white-space: nowrap;
  }
  .main-nav a.is-current { background: var(--purple-deep); }

  /* Hero */
  .hero-image {
    position: absolute; left: 111px; top: 140px; width: 479px; height: 440px;
    background: radial-gradient(ellipse 44% 42% at 48% 46%, var(--hero-green) 0%, #b7cc8e 55%, var(--hero-light) 100%);
  }
  .hero-title {
    position: absolute; right: 471px; top: 489px; height: 48px;
    background: rgba(255,255,255,0.95);
    font-family: "Fira Sans Extra Condensed", sans-serif; font-weight: 500;
    font-size: 30px; line-height: 48px; white-space: nowrap;
    padding: 0 12px 0 13px;
    color: var(--purple-title);
  }
  .hero-text {
    position: absolute; left: 379px; top: 541px; width: 350px; height: 79px;
    background: rgba(255,255,255,0.95);
    padding: 8px 14px 0 18px;
    font-size: 13px; line-height: 20px; color: var(--ink); text-align: justify;
    text-indent: 4px;
  }
  .slider-dots { position: absolute; left: 121px; top: 628px; display: flex; gap: 4px; }
  .slider-dots span {
    width: 12px; height: 12px; border-radius: 50%;
    background: var(--purple-panel); border: 1px solid #7a6088;
  }
  .slider-dots span.is-empty { background: var(--white); border-color: #999; }

  /* Member panel */
  .member-frame {
    position: absolute; left: 743px; top: 140px; width: 337px; height: 479px;
    background: var(--panel-frame);
  }
  .member-panel {
    position: absolute; left: 752px; top: 149px; width: 318px; height: 460px;
    background: var(--purple-panel);
  }
  .panel-heading {
    position: absolute; left: 22px;
    display: flex; align-items: center; gap: 10px;
    font-family: "Fira Sans Extra Condensed", sans-serif; font-weight: 600;
    font-size: 21px; color: var(--white); white-space: nowrap;
  }
  .field {
    position: absolute; left: 23px; width: 272px; height: 33px;
    border: 1px solid #cfc4d6; background: var(--white);
    font-family: inherit; font-size: 11px; padding-left: 14px; color: var(--ink);
  }
  .field::placeholder { color: var(--field-text); }
  .panel-button {
    position: absolute; left: 223px; width: 74px; height: 31px;
    border-radius: 10px; border: 2px solid #b49cc3;
    background: linear-gradient(#8a6b9d, #5e4571);
    color: var(--white); font-family: inherit; font-weight: 700; font-size: 11px;
  }
  .panel-divider {
    position: absolute; left: 6px; top: 205px; width: 307px; height: 0;
    border-top: 1px solid #6f527f; border-bottom: 1px solid #a58cb3;
  }

  /* Footer */
  .site-footer {
    position: absolute; left: 0; top: 667px; width: 1200px; height: 101px;
    background: linear-gradient(var(--purple-top), var(--purple-bottom));
    border-top: 2px solid #b9a6c6;
    font-family: Arial, sans-serif; font-size: 12px; color: var(--white);
  }
  .footer-nav { position: absolute; left: 111px; top: 22px; white-space: nowrap; }
  .footer-nav a { color: var(--white); text-decoration: none; }
  .footer-nav .sep { margin: 0 10px; }
  .copyright { position: absolute; left: 111px; top: 51px; white-space: nowrap; }
  .social-links { position: absolute; left: 924px; top: 46px; display: flex; gap: 12px; }
  .social-links a {
    display: flex; align-items: center; gap: 5px;
    color: var(--white); text-decoration: none; font-family: "Source Sans 3", sans-serif;
    font-size: 13px; font-weight: 600;
  }
  .social-links .dot { width: 14px; height: 14px; border-radius: 50%; }
</style>
</head>
<body>
  <header class="site-header">
    <div class="brand">THORNVALE</div>
    <nav class="main-nav">
      <a href="#" class="is-current">Home</a>
      <a href="#">About</a>
      <a href="#">Register</a>
      <a href="#">Log in</a>
      <a href="#">Help</a>
    </nav>
  </header>

  <main>
    <div class="hero-image" role="img" aria-label="Photo of a tree whose leafy crown forms a globe of the world"></div>
    <h1 class="hero-title">WELCOME TO THORNVALE</h1>
    <p class="hero-text">Fusce id libero quis eros lobortis condimentum. Maecenas id sodales quam. Donec ac dui nec mauris scelerisque adipiscing. Ut eleifend nunc vel nisl aliquet placerat.</p>
    <div class="slider-dots"><span></span><span></span><span class="is-empty"></span></div>

    <div class="member-frame"></div>
    <section class="member-panel">
      <h2 class="panel-heading" style="top:16px">
        <svg width="24" height="30" viewBox="0 0 24 30" aria-hidden="true">
          <path d="M6 13 V9 a6 6 0 0 1 12 0 V13" fill="none" stroke="#c9c9cc" stroke-width="3"/>
          <rect x="2" y="13" width="20" height="16" rx="2" fill="#a9a9ad"/>
          <rect x="2" y="13" width="20" height="5" rx="2" fill="#d4d4d8"/>
        </svg>
        MEMBER LOGIN
      </h2>
      <input class="field" style="top:59px" type="text" placeholder="Username">
      <input class="field" style="top:109px" type="password" placeholder="********">
      <button class="panel-button" style="top:152px">LOG IN</button>

      <div class="panel-divider"></div>

      <h2 class="panel-heading" style="top:226px">
        <svg width="24" height="30" viewBox="0 0 24 30" aria-hidden="true">
          <circle cx="12" cy="9" r="6" fill="#e3a86a"/>
          <path d="M2 29 C2 19 22 19 22 29 Z" fill="#9a9aa0"/>
        </svg>
        MEMBER SIGNUP
      </h2>
      <input class="field" style="top:269px" type="email" placeholder="Email">
      <input class="field" style="top:319px" type="password" placeholder="Password">
      <input class="field" style="top:370px" type="password" placeholder="Confirm Password">
      <button class="panel-button" style="top:412px">SIGN UP</button>
    </section>
  </main>

  <footer class="site-footer">
    <nav class="footer-nav">
      <a href="#">Home</a><span class="sep">|</span><a href="#">About</a><span class="sep">|</span><a href="#">Register</a><span class="sep">|</span><a href="#">Log in</a><span class="sep">|</span><a href="#">Help</a>
    </nav>
    <p class="copyright">Copyright &copy; &nbsp;2013 &nbsp;www.thornvale.com &nbsp;&nbsp;| &nbsp;&nbsp;All rights reserved.</p>
    <div class="social-links">
      <a href="#"><span class="dot" style="background:var(--social-1)"></span>Linkora</a>
      <a href="#"><span class="dot" style="background:var(--social-2)"></span>Chirply</a>
      <a href="#"><span class="dot" style="background:var(--social-3)"></span>Vidzio</a>
    </div>
  </footer>
</body>
</html>
```